We need a web page design for a new company called "Brindle". We provide an innovative music sharing mobile application that allows music listeners to share their music without paying for a monthly subscription. We would like to incorporate the attached logo and color scheme. The final design should communicate music gifting and sharing.

Industry/Entity Type

It Company

```html
<!DOCTYPE html>
<html lang="en">
<head>
<meta charset="UTF-8">
<title>Brindle</title>
<link rel="stylesheet" href="https://fonts.googleapis.com/css2?family=Oswald:wght@300;400&family=Open+Sans:ital,wght@0,400;0,600;1,400&display=swap">
<style>
  :root {
    --green: #5ea80a;
    --red: #d9513e;
    --yellow: #e0c414;
    --tile-green: #6aaa1c;
    --tile-red: #dd5a4a;
    --strip: #3a3a3a;
    --footer: #111111;
    --white: #ffffff;
    --muted: #dddddd;
  }
  * { box-sizing: border-box; margin: 0; padding: 0; }
  html, body { width: 1200px; height: 961px; overflow: hidden; background: #000; }
  .page { position: relative; width: 1200px; height: 961px; overflow: hidden; font-family: "Open Sans", sans-serif; color: var(--white); }

  .hero-photo {
    position: absolute; left: 0; top: 0; width: 1200px; height: 720px;
    background:
      radial-gradient(ellipse at 42% 8%, #e9c7a6 0%, #b9826a 22%, transparent 55%),
      radial-gradient(ellipse at 80% 30%, #8a3a2a 0%, transparent 50%),
      linear-gradient(180deg, #9b6a52 0%, #6b3d2c 40%, #2a150e 75%, #0b0604 100%);
  }

  .brand-box {
    position: absolute; left: 0; top: 25px; width: 255px; height: 97px;
    background: var(--green); display: flex; align-items: center; justify-content: center;
  }
  .brand-name { font-family: "Oswald", sans-serif; font-weight: 400; font-size: 44px; line-height: 1; letter-spacing: 1px; color: var(--white); }

  .main-nav {
    position: absolute; left: 521px; top: 30px; width: 679px; height: 88px;
    background: var(--green); display: flex; align-items: center; justify-content: space-around; padding: 0 8px;
    font-family: "Oswald", sans-serif; font-weight: 300; font-size: 18px; letter-spacing: 0.3px;
  }

  .social-row { position: absolute; left: 523px; top: 133px; display: flex; gap: 27.5px; }
  .social-dot { width: 20px; height: 20px; border-radius: 50%; background: var(--white); opacity: 0.92; }

  .account { position: absolute; top: 128px; height: 27px; font-size: 12px; display: flex; align-items: center; justify-content: center; }
  .account.login { left: 1052px; width: 58px; background: var(--green); }
  .account.signin { left: 1117px; width: 58px; background: var(--red); }

  .caption { position: absolute; left: 0; font-family: "Oswald", sans-serif; font-weight: 300; display: flex; align-items: center; padding-left: 22px; letter-spacing: 0.5px; }
  .caption.title { top: 432px; width: 377px; height: 51px; background: var(--red); font-size: 30px; padding-bottom: 4px; }
  .caption.sub { top: 487px; width: 187px; height: 51px; background: var(--green); font-size: 24px; padding-bottom: 3px; }

  .slider-btn { position: absolute; top: 440px; width: 48px; height: 37px; background: var(--green); display: flex; align-items: center; justify-content: center; }
  .slider-btn.prev { left: 1099px; background: rgba(94,168,10,0.7); }
  .slider-btn.next { left: 1151px; }

  .features { position: absolute; top: 720px; left: 0; width: 1200px; height: 101px; display: flex; }
  .feature { flex: none; display: flex; align-items: center; justify-content: center; font-family: "Oswald", sans-serif; font-size: 26px; letter-spacing: 1px; }
  .feature.yellow { width: 401px; background: linear-gradient(90deg, var(--yellow), #c9ab10 60%, var(--yellow)); }
  .feature.green { width: 399px; background: linear-gradient(90deg, var(--tile-green), #7cb82c 50%, var(--tile-green)); }
  .feature.red { width: 400px; background: linear-gradient(90deg, var(--tile-red), #c9584a 50%, var(--tile-red)); }

  .summaries { position: absolute; top: 821px; left: 0; width: 1200px; height: 61px; background: var(--strip); display: flex; font-size: 13px; color: var(--muted); }
  .summary { display: flex; align-items: center; }
  .summary.left { width: 641px; padding-left: 45px; border-right: 1px solid #555; }
  .summary.right { width: 559px; justify-content: flex-end; padding-right: 40px; }

  .site-footer { position: absolute; top: 882px; left: 0; width: 1200px; height: 79px; background: var(--footer); }
  .footer-links { position: absolute; left: 22px; top: 19px; font-family: "Oswald", sans-serif; font-weight: 300; font-size: 13px; word-spacing: 2px; }
  .copyright { position: absolute; left: 22px; top: 42px; font-family: "Oswald", sans-serif; font-weight: 300; font-size: 12px; }
  .footer-brand { position: absolute; left: 444px; top: 16px; width: 162px; text-align: center; }
  .footer-brand .brand-name { font-size: 36px; }
  .newsletter-title { position: absolute; left: 706px; top: 18px; font-family: "Oswald", sans-serif; font-size: 28px; letter-spacing: -0.3px; }
  .newsletter-form { position: absolute; left: 918px; top: 18px; width: 249px; height: 42px; background: var(--white); border-radius: 3px; }
  .newsletter-input { position: absolute; left: 13px; top: 13px; font-size: 11px; font-style: italic; color: #999; }
  .newsletter-btn { position: absolute; left: 143px; top: 6px; width: 98px; height: 29px; background: var(--red); font-size: 12px; font-weight: 600; letter-spacing: 0.5px; display: flex; align-items: center; justify-content: center; }
</style>
</head>
<body>
<div class="page">
  <div class="hero-photo" role="img" aria-label="Concert crowd with raised hands under warm stage lights"></div>

  <header>
    <div class="brand-box">
      <span class="brand-name">Brindle</span>
    </div>
    <nav class="main-nav">
      <span>HOME</span><span>EVENTS</span><span>ALBUMS</span><span>GALLERY</span><span>BLOG</span><span>FEATURES</span><span>SHOP</span>
    </nav>
    <div class="social-row" aria-label="Social links">
      <span class="social-dot"></span><span class="social-dot"></span><span class="social-dot"></span><span class="social-dot"></span>
      <span class="social-dot"></span><span class="social-dot"></span><span class="social-dot"></span><span class="social-dot"></span>
      <span class="social-dot"></span><span class="social-dot"></span><span class="social-dot"></span>
    </div>
    <div class="account login">LOGIN</div>
    <div class="account signin">SING IN</div>
  </header>

  <section>
    <div class="caption title">Share Your Songs With Brindle</div>
    <div class="caption sub">and then enjoy...</div>
    <div class="slider-btn prev"><svg width="14" height="24" viewBox="0 0 14 24"><polyline points="12,2 2,12 12,22" fill="none" stroke="#fff" stroke-width="1.6"/></svg></div>
    <div class="slider-btn next"><svg width="14" height="24" viewBox="0 0 14 24"><polyline points="2,2 12,12 2,22" fill="none" stroke="#fff" stroke-width="1.6"/></svg></div>
  </section>

  <section class="features">
    <div class="feature yellow" role="img" aria-label="Singer performing on stage">Ironleaf Live in Texus</div>
    <div class="feature green" role="img" aria-label="Festival crowd">Vocal Summer Festival Begins</div>
    <div class="feature red" role="img" aria-label="Band playing to an audience">The Marlow Brothers Give Brooklyn</div>
  </section>

  <section class="summaries">
    <div class="summary left">Pastrami venison shankle tenderloin boudin prosciutto pork chop. Corned beef</div>
    <div class="summary right">Pastrami venison shankle tenderloin boudin prosciutto pork chop.</div>
  </section>

  <footer class="site-footer">
    <div class="footer-links">HOME &nbsp;| EVENTS &nbsp;| &nbsp;BLOG &nbsp;| &nbsp;FEATURES</div>
    <div class="copyright">© 2014 Brindle All rights reserved.</div>
    <div class="footer-brand"><span class="brand-name">Brindle</span></div>
    <div class="newsletter-title">Singup Newsletter</div>
    <div class="newsletter-form">
      <span class="newsletter-input">Your Email Address</span>
      <span class="newsletter-btn">SUBSCRIBE</span>
    </div>
  </footer>
</div>
</body>
</html>
```